Flyer für Freie Referentin
I thank Merak Tuwero for the great work! I’am very satisfied with the design of my flyer, with the arrangement of the photos, the font and the colors. Everything is fine and exactly as I imagined before. All my requested changings were changed very quickly and correctly. I would definitely recommend this designer!
Zielgruppe
Ich biete Vorträge, Kurse, Fortbildungen und Privatunterricht an zu den Themen:
Einführung in die Weltreligionen
und
Feste der Religionen
Außerdem biete ich Führungen durch religiöse Gebäude in Berlin an.
Meine Zielgruppen sind:
1. Pädagogen in Kita, Grund-und Oberschule,
2. Religionslehrer,
3.Fachkräfte im interkulturellen Kontext (Ausländerbehörde, Gesundheitswesen, Sozialwesen) und
4. Menschen, die gern reisen und sich für andere Religionen und Kulturen interessieren
Aufgabenstellung
Ich habe selbst einen 6 seitigen Falzflyer entworfen, mit Text und Bildern und würde diesen inhaltlich weitgehend so lassen, und nur in einem ansprechenden Design umgestalten lassen. Die Fotos, die ich liefere, habe ich in den religiösen Gebäuden selbst gemacht.

```html
<!DOCTYPE html>
<html lang="de">
<head>
<meta charset="utf-8">
<title>Weltreligionen verstehen – Flyer</title>
<link href="https://fonts.googleapis.com/css2?family=Anton&family=Arimo:wght@400;700&display=swap" rel="stylesheet">
<style>
  :root {
    --paper: #f1ecdc;
    --ink: #111111;
    --text: #1c1c1c;
    --gold: #c9a13c;
    --sky: #8fb3d6;
    --stone: #b8a78d;
    --festive: #a86a7a;
    --hall: #9a8f86;
    --flame: #5f7a34;
  }
  * { margin: 0; padding: 0; box-sizing: border-box; }
  html, body { width: 1200px; height: 856px; overflow: hidden; background: var(--paper); }
  .flyer { position: relative; width: 1200px; height: 856px; background: var(--paper); color: var(--text);
    font-family: "Arimo", Arial, sans-serif; font-size: 17.5px; line-height: 22.3px; }
  .block { position: absolute; }
  .heading { font-family: "Anton", "Impact", sans-serif; font-weight: 400; font-size: 29.5px; line-height: 36px;
    color: var(--ink); text-transform: uppercase; letter-spacing: -0.2px; }
  .list { list-style: none; }
  .list li { position: relative; padding-left: 16px; }
  .list li::before { content: "•"; position: absolute; left: 0; font-size: 13px; }
  .sub { font-weight: 700; color: var(--ink); }
  .note { padding-left: 21px; }
  .photo { position: absolute; }
</style>
</head>
<body>
<main class="flyer">

  <!-- Spalte 1 -->
  <h2 class="block heading" style="left:36px; top:96px; width:340px;">Weltreligionen verstehen -<br>Menschen besser begegnen<br>Mein Angebot</h2>
  <ul class="block list" style="left:36px; top:211px; width:330px;">
    <li>Vorträge &amp; Seminare zu:<br>Judentum, Christentum, Islam,<br>Hinduismus und Buddhismus</li>
    <li>Vorträge &amp; Seminare zu religiösen<br>Festen und Traditionen</li>
    <li>Besuche religiöser Stätten</li>
    <li>Individuelle Weiterbildungen &amp;<br>Privatunterricht</li>
  </ul>

  <h2 class="block heading" style="left:36px; top:449px; width:340px;">Welche Themen biete ich an?</h2>
  <p class="block sub" style="left:36px; top:499px;">1.&nbsp; Einführung Weltreligionen</p>
  <ul class="block list" style="left:36px; top:543px; width:220px;">
    <li>Herkunft &amp; Heilige<br>Schrift</li>
    <li>Lehren &amp; Rituale</li>
    <li>Ethik &amp; Verhalten</li>
  </ul>
  <p class="block sub" style="left:36px; top:655px;">2. Feste in den Religionen</p>
  <ul class="block list" style="left:36px; top:699px; width:220px;">
    <li>Kalender &amp; Anlässe</li>
    <li>Geschichten &amp; Musik</li>
    <li>Rituale &amp; Speisen</li>
  </ul>
  <svg class="photo" style="left:270px; top:547px;" width="102" height="100" role="img" aria-label="Foto: Menschen tanzen gemeinsam bei einem religiösen Fest im Freien">
    <defs><linearGradient id="gDance" x1="0" y1="0" x2="0" y2="1"><stop offset="0" stop-color="#9a8c8a"/><stop offset="1" stop-color="var(--festive)"/></linearGradient></defs>
    <rect width="102" height="100" fill="url(#gDance)"/>
  </svg>
  <svg class="photo" style="left:270px; top:655px;" width="102" height="101" role="img" aria-label="Foto: Gemeinsames Festessen an langen Tischen in einem Saal">
    <defs><linearGradient id="gMeal" x1="0" y1="0" x2="0" y2="1"><stop offset="0" stop-color="#c9ccd0"/><stop offset="1" stop-color="var(--hall)"/></linearGradient></defs>
    <rect width="102" height="101" fill="url(#gMeal)"/>
  </svg>

  <!-- Spalte 2 -->
  <h2 class="block heading" style="left:419px; top:96px; width:340px;">Besuch religiöser Stätten</h2>
  <ul class="block list" style="left:419px; top:151px; width:320px;">
    <li>Führung durch die Räume</li>
    <li>Teilnahme an Zeremonien</li>
    <li>Austausch mit Gläubigen</li>
  </ul>
  <svg class="photo" style="left:419px; top:245px;" width="93" height="164" role="img" aria-label="Foto: Goldener Tempelturm eines Hindu-Tempels">
    <defs><linearGradient id="gTemple" x1="0" y1="0" x2="0" y2="1"><stop offset="0" stop-color="#b7a889"/><stop offset="1" stop-color="var(--gold)"/></linearGradient></defs>
    <rect width="93" height="164" fill="url(#gTemple)"/>
  </svg>
  <svg class="photo" style="left:520px; top:245px;" width="130" height="86" role="img" aria-label="Foto: Moschee mit Kuppel und Minaretten vor blauem Himmel">
    <defs><linearGradient id="gMosque" x1="0" y1="0" x2="0" y2="1"><stop offset="0" stop-color="var(--sky)"/><stop offset="1" stop-color="#dcdcd6"/></linearGradient></defs>
    <rect width="130" height="86" fill="url(#gMosque)"/>
  </svg>
  <svg class="photo" style="left:520px; top:337px;" width="130" height="72" role="img" aria-label="Foto: Innenraum einer Moschee mit Gebetsnische und Fliesen">
    <defs><linearGradient id="gInterior" x1="0" y1="0" x2="1" y2="0"><stop offset="0" stop-color="#8a9aa8"/><stop offset="0.5" stop-color="var(--stone)"/><stop offset="1" stop-color="#7f95a6"/></linearGradient></defs>
    <rect width="130" height="72" fill="url(#gInterior)"/>
  </svg>

  <h2 class="block heading" style="left:419px; top:449px; width:340px;">Was Sie mitnehmen</h2>
  <ul class="block list" style="left:419px; top:498px; width:320px;">
    <li>Klar verständliches Wissen zu den<br>Weltreligionen</li>
    <li>Hintergründe zu Festen, Bräuchen<br>und Symbolen</li>
    <li>Aha-Momente für Beruf, Alltag und<br>Reisen</li>
  </ul>
  <svg class="photo" style="left:419px; top:648px;" width="219" height="108" role="img" aria-label="Foto: Hände halten eine Tonschale mit Feuer bei einer Zeremonie">
    <defs><linearGradient id="gFire" x1="0" y1="0" x2="1" y2="0"><stop offset="0" stop-color="var(--flame)"/><stop offset="0.5" stop-color="#a4552c"/><stop offset="1" stop-color="#8fa05a"/></linearGradient></defs>
    <rect width="219" height="108" fill="url(#gFire)"/>
  </svg>

  <!-- Spalte 3 -->
  <h2 class="block heading" style="left:816px; top:96px; width:340px;">Meine Angebote richten<br>sich an</h2>
  <p class="block sub" style="left:816px; top:197px;">1. Lehrkräfte allgemein</p>
  <ul class="block list" style="left:816px; top:241px; width:360px;">
    <li>Gewinnen Sie fundiertes Wissen, um<br><b>Schüler*innen unterschiedlicher<br>Herkunft</b> besser zu begleiten</li>
  </ul>
  <p class="block sub" style="left:816px; top:350px;">2. Religionslehrer*innen</p>
  <ul class="block list" style="left:816px; top:395px; width:360px;">
    <li>Vertiefen Sie Ihr Wissen zu Inhalten<br>der großen Religionen – praxisnah<br>und aktuell!</li>
  </ul>
  <p class="block sub" style="left:816px; top:509px;">3. Fachkräfte im interkulturellen Kontext</p>
  <p class="block note" style="left:816px; top:532px;">(Ausländerbehörde, Asylberatung,<br>Gesundheitswesen)</p>
  <ul class="block list" style="left:816px; top:598px; width:360px;">
    <li>Gewinnen Sie Sicherheit im Umgang mit<br>religiös geprägten Verhaltensweisen!</li>
  </ul>
  <p class="block sub" style="left:816px; top:698px;">4. Reisefreudige &amp; Neugierige</p>
  <ul class="block list" style="left:816px; top:721px; width:360px;">
    <li>Entdecken Sie spannende Einblicke in<br>Rituale, Werte und Feiertage weltweit!</li>
  </ul>

</main>
</body>
</html>
```